Business Card for Managing Partner Investment Fund

To create a business card template for an investment fund manager. Business card should be more professional in nature, not too colorful, more upscale, and created using the attached logos and fund name files. I would prefer a black or gray color scheme, but am open to the use of color as well. I would prefer a double sided business card, but open to single sided business card designs as well. The business card should include: name, title, and contact information, as well as logo and company name. I would prefer a more stream-lined, simple business card design.
Updates
Address: 4190 NE 38th Ter. Ocala, FL 34470
Email: talvin47@quorimail.net
Phone: 561-347-9162
Title: managing partner
Name: Dorian Velsky
Fund Name: Ambergate Capital
Logos can be found in files attached to the brief
Target Market(s)
potential investors, other fund managers
Industry/Entity Type
Finance
Contact Information for Business Card
Name on card: Dorian Velsky
Title: Managing Partner
Colors
Designer to choose colors to be used in the design.
Requirements
Must have
- Phone number
- email address
- physical address
- title
- name
- logo
- Fund name
Nice to have
- simple layout
Should not have
- too many colors, busy fonts,

```html
<!DOCTYPE html>
<html lang="en">
<head>
<meta charset="utf-8">
<title>Ambergate Capital – Business Card</title>
<link href="https://fonts.googleapis.com/css2?family=Roboto:wght@400;500&display=swap" rel="stylesheet">
<style>
  :root {
    --canvas-bg: #e8e6e3;
    --card-white: #ffffff;
    --card-grey: #5e5e5e;
    --ink-dark: #333333;
    --ink-mid: #555555;
    --brand-grey: #6a6a6a;
    --rule: #777777;
    --on-dark: #ffffff;
  }
  * { margin: 0; padding: 0; box-sizing: border-box; }
  html, body {
    width: 1200px; height: 1200px; overflow: hidden;
    background: var(--canvas-bg);
    font-family: "Roboto", Arial, sans-serif;
  }
  .card {
    position: absolute; left: 214px; width: 772px; height: 440px;
    box-shadow: 0 3px 10px rgba(0,0,0,0.18);
  }
  .card--front { top: 150px; background: var(--card-white); }
  .card--back { top: 633px; background: var(--card-grey); }

  .front-brand {
    position: absolute; left: 40px; width: 330px; top: 196px;
    text-align: center; color: var(--brand-grey); font-weight: 400;
  }
  .front-brand__name { font-size: 34px; letter-spacing: 2px; line-height: 1; }
  .front-brand__sub { font-size: 20px; letter-spacing: 5px; margin-top: 8px; }

  .divider {
    position: absolute; left: 388px; top: 102px; width: 1.5px; height: 238px;
    background: var(--rule);
  }

  .details { position: absolute; left: 424px; top: 88px; color: var(--ink-mid); }
  .details__name { font-size: 29px; font-weight: 500; color: var(--ink-dark); line-height: 1.1; }
  .details__title { font-size: 20px; margin-top: 4px; }
  .details__address { font-size: 18.5px; line-height: 26px; margin-top: 18px; }
  .contact-list { list-style: none; margin-top: 14px; font-size: 18.5px; }
  .contact-list li { display: flex; align-items: center; height: 27.5px; }
  .contact-list svg { width: 16px; height: 16px; margin-right: 7px; flex: none; }

  .back-brand {
    position: absolute; left: 0; right: 0; top: 150px;
    text-align: center; color: var(--on-dark); font-weight: 400;
  }
  .back-brand__name { font-size: 58px; letter-spacing: 4px; line-height: 1; }
  .back-brand__sub { font-size: 36px; letter-spacing: 8px; margin-top: 18px; }
</style>
</head>
<body>
  <section class="card card--front">
    <div class="front-brand">
      <div class="front-brand__name">AMBERGATE</div>
      <div class="front-brand__sub">CAPITAL</div>
    </div>
    <div class="divider"></div>
    <div class="details">
      <div class="details__name">Dorian Velsky</div>
      <div class="details__title">Managing Partner</div>
      <div class="details__address">4190 NE 38th Ter.<br>Ocala, FL 34470</div>
      <ul class="contact-list">
        <li>
          <svg viewBox="0 0 16 16" fill="none" stroke="#555" stroke-width="1.2"><path d="M3 1.5h3l1.3 3.4-1.8 1.2a8 8 0 0 0 4.4 4.4l1.2-1.8 3.4 1.3v3a1.5 1.5 0 0 1-1.6 1.5A13 13 0 0 1 1.5 3.1 1.5 1.5 0 0 1 3 1.5z"/></svg>
          561-347-9162
        </li>
        <li>
          <svg viewBox="0 0 16 16" fill="none" stroke="#555" stroke-width="1.2"><rect x="4" y="1" width="8" height="14" rx="1.3"/><line x1="7" y1="12.5" x2="9" y2="12.5"/></svg>
          561-347-9185
        </li>
        <li>
          <svg viewBox="0 0 16 16" fill="none" stroke="#555" stroke-width="1.2"><rect x="1.5" y="3.5" width="13" height="9"/><path d="M1.5 3.5 8 9l6.5-5.5"/></svg>
          talvin47@quorimail.net
        </li>
        <li>
          <svg viewBox="0 0 16 16" fill="none" stroke="#555" stroke-width="1.1"><circle cx="8" cy="8" r="6.5"/><ellipse cx="8" cy="8" rx="3" ry="6.5"/><line x1="1.5" y1="8" x2="14.5" y2="8"/><path d="M2.6 4.5h10.8M2.6 11.5h10.8"/></svg>
          www.ambergatecap.net
        </li>
      </ul>
    </div>
  </section>

  <section class="card card--back">
    <div class="back-brand">
      <div class="back-brand__name">AMBERGATE</div>
      <div class="back-brand__sub">CAPITAL</div>
    </div>
  </section>
</body>
</html>
```